Bradwell Business Card

I have a logo that I would like to use to design the Business Card for Bradwell Construction LLC. We are a commercial general contractor in San Antonio Texas. Id like a simple and sleek design. Message me if you have any questions. Thanks

Industry/Entity Type

Contractor

```html
<!DOCTYPE html>
<html lang="en">
<head>
<meta charset="utf-8">
<title>Bradwell Construction LLC – Business Card</title>
<link rel="stylesheet" href="https://fonts.googleapis.com/css2?family=Roboto+Condensed:wght@400;700&family=Saira+Semi+Condensed:wght@500;600&display=swap">
<style>
  :root {
    --page-bg: #e6e8eb;
    --card-top: #ffffff;
    --card-bottom: #e9eaec;
    --ink: #2b2b2b;
    --brand-blue: #3a6ab8;
    --band-dark: #2f5ba3;
    --stripe-grey: #dcdde0;
    --white: #ffffff;
  }
  * { box-sizing: border-box; margin: 0; padding: 0; }
  html, body {
    width: 1028px; height: 1200px; overflow: hidden;
    background: var(--page-bg);
    font-family: "Roboto Condensed", "Arial Narrow", sans-serif;
  }
  .card {
    position: absolute; left: 84px; width: 860px; height: 500px;
    background: linear-gradient(160deg, var(--card-top) 40%, var(--card-bottom) 100%);
    box-shadow: 0 6px 18px rgba(0,0,0,0.18);
    overflow: hidden;
  }
  .card--front { top: 70px; }
  .card--back { top: 630px; }

  .brand { position: absolute; display: flex; align-items: center; gap: 22px; }
  .brand__square { width: 56px; height: 56px; background: var(--brand-blue); flex: none; }
  .brand__name {
    font-weight: 700; color: var(--ink); text-transform: uppercase;
    line-height: 0.95; letter-spacing: 0.5px; white-space: nowrap;
  }
  .brand__line { display: block; }

  .card--front .brand { left: 50%; top: 50%; transform: translate(-50%, -50%); }
  .card--front .brand__name { font-size: 50px; }

  .back__stripe {
    position: absolute; left: 78px; top: 0; width: 32px; height: 100%;
    background: var(--stripe-grey);
  }
  .card--back .brand {
    left: 150px; top: 36px; flex-direction: column; gap: 26px;
  }
  .card--back .brand__square { width: 72px; height: 72px; }
  .card--back .brand__name { font-size: 38px; }

  .person {
    position: absolute; right: 42px; top: 160px; text-align: right;
    font-family: "Saira Semi Condensed", "Arial Narrow", sans-serif;
  }
  .person__name { font-size: 42px; font-weight: 600; color: var(--brand-blue); letter-spacing: 1px; line-height: 1; white-space: nowrap; }
  .person__title { margin-top: 10px; font-size: 14px; font-weight: 500; color: var(--brand-blue); letter-spacing: 1.5px; text-transform: uppercase; }

  .contact-band {
    position: absolute; left: 0; top: 300px; width: 100%; height: 148px;
    background: var(--brand-blue);
  }
  .contact-band__address-row {
    position: absolute; left: 0; top: 58px; width: 100%; height: 40px;
    background: var(--band-dark);
  }
  .contact { position: absolute; left: 88px; display: flex; align-items: center; gap: 12px; color: var(--white); font-size: 14px; letter-spacing: 0.3px; white-space: nowrap; }
  .contact svg { width: 14px; height: 14px; flex: none; }
</style>
</head>
<body>

<section class="card card--front" aria-label="Business card front">
  <div class="brand">
    <span class="brand__square"></span>
    <span class="brand__name"><span class="brand__line">Bradwell</span><span class="brand__line">Construction LLC</span></span>
  </div>
</section>

<section class="card card--back" aria-label="Business card back">
  <div class="back__stripe"></div>

  <div class="brand">
    <span class="brand__square"></span>
    <span class="brand__name"><span class="brand__line">Bradwell</span><span class="brand__line">Construction LLC</span></span>
  </div>

  <div class="person">
    <p class="person__name">DANIEL REYES</p>
    <p class="person__title">General Manager</p>
  </div>

  <div class="contact-band">
    <div class="contact-band__address-row"></div>

    <p class="contact" style="top:10px">
      <svg viewBox="0 0 16 16" aria-hidden="true"><path fill="#fff" d="M3 1l3 3-1.5 2a9 9 0 0 0 5.5 5.5L12 10l3 3-2 2C7 15 1 9 1 3z"/></svg>
      210 555 0147
    </p>
    <p class="contact" style="top:32px">
      <svg viewBox="0 0 16 16" aria-hidden="true"><rect x="4" y="1" width="8" height="14" rx="1.5" fill="none" stroke="#fff" stroke-width="1.6"/><circle cx="8" cy="12.5" r="0.9" fill="#fff"/></svg>
      210 555 0148
    </p>
    <p class="contact" style="top:69px">
      <svg viewBox="0 0 16 16" aria-hidden="true"><path fill="#fff" d="M8 1a5 5 0 0 0-5 5c0 4 5 9 5 9s5-5 5-9a5 5 0 0 0-5-5zm0 7a2 2 0 1 1 0-4 2 2 0 0 1 0 4z"/></svg>
      4200 Broadway Street, Suite 3, San Antonio
    </p>
    <p class="contact" style="top:106px">
      <svg viewBox="0 0 16 16" aria-hidden="true"><rect x="1" y="3" width="14" height="10" rx="1" fill="none" stroke="#fff" stroke-width="1.5"/><path d="M1.5 3.5L8 9l6.5-5.5" fill="none" stroke="#fff" stroke-width="1.5"/></svg>
      info@bradwellbuilds.com
    </p>
    <p class="contact" style="top:126px">
      <svg viewBox="0 0 16 16" aria-hidden="true"><circle cx="8" cy="8" r="6.5" fill="none" stroke="#fff" stroke-width="1.4"/><ellipse cx="8" cy="8" rx="2.8" ry="6.5" fill="none" stroke="#fff" stroke-width="1.2"/><path d="M1.5 8h13" stroke="#fff" stroke-width="1.2"/></svg>
      www.bradwellbuilds.com
    </p>
  </div>
</section>

</body>
</html>
```